Author book launch promotion design for social media

We are organising an authors book launch event and require an author promotion design that will be used on social media (Chatterly, netwise) promotion.

The design must have the author's photo, image of their book, the event logo, details of the event plus website address (quillfairhub.com.au).

Details of the event can be found at quillfairhub.com.au.

the design has to be attractive and inviting and colours in accordance with the brand colours.

You can choose 1 one of the book images attached
Author name: Dr Tobias Merrill
Event Details
LAUNCH YOUR BOOK IN STYLE

Pagecraft Reading Fair 2022
7 - 8 October 2022
Melbourne Larkfield Pavilion
14 Corrigan St, Southbank Melbourne

For registration and ticketing visit:
quillfairhub.com.au

I have attached also a sample promo. Please be creative.

```html
<!DOCTYPE html>
<html lang="en">
<head>
<meta charset="utf-8">
<title>Launch Your Book in Style – Pagecraft Reading Fair 2022</title>
<link rel="stylesheet" href="https://fonts.googleapis.com/css2?family=Montserrat:wght@500;600;700;800;900&family=Mrs+Saint+Delafield&display=swap">
<style>
  :root {
    --stage: #a9b7c8;
    --navy: #0f2a46;
    --navy-deep: #0b2036;
    --white: #ffffff;
    --gold: #f1ae3d;
    --pink: #d42a5b;
    --band: #ebebeb;
    --cover-light: #e9e9ea;
    --cover-mid: #b9bcc2;
  }
  * { margin: 0; padding: 0; box-sizing: border-box; }
  html, body {
    width: 1200px; height: 678px; overflow: hidden;
    background: var(--stage);
    font-family: "Montserrat", sans-serif;
  }
  .promo-post {
    position: absolute; left: 280px; top: 19px;
    width: 640px; height: 640px;
  }
  .promo-post svg { display: block; width: 640px; height: 640px; }
  .headline { font-family: "Montserrat", sans-serif; font-weight: 900; fill: var(--white); }
  .tag-your { font-family: "Montserrat", sans-serif; font-weight: 900; fill: var(--navy); font-size: 17px; }
  .script-style { font-family: "Mrs Saint Delafield", cursive; fill: var(--pink); }
  .event-name { font-family: "Montserrat", sans-serif; font-weight: 900; fill: var(--gold); font-size: 37px; }
  .brand-name { font-family: "Montserrat", sans-serif; font-weight: 800; fill: var(--gold); }
  .author-name { font-family: "Montserrat", sans-serif; font-weight: 800; fill: var(--pink); font-size: 18px; }
  .detail-large { font-family: "Montserrat", sans-serif; font-weight: 600; fill: var(--white); font-size: 23px; letter-spacing: -0.8px; }
  .detail-small { font-family: "Montserrat", sans-serif; font-weight: 600; fill: var(--white); font-size: 14.5px; letter-spacing: -0.5px; }
  .ticket-text { font-family: "Montserrat", sans-serif; font-weight: 600; fill: var(--white); font-size: 15px; letter-spacing: -0.4px; }
</style>
</head>
<body>
<main class="promo-post">
  <svg viewBox="0 0 640 640" xmlns="http://www.w3.org/2000/svg" aria-label="Launch your book in style – Pagecraft Reading Fair 2022 promotion">
    <defs>
      <linearGradient id="coverTone" x1="0" y1="0" x2="0" y2="1">
        <stop offset="0" stop-color="var(--cover-light)"/>
        <stop offset="0.55" stop-color="var(--cover-mid)"/>
        <stop offset="1" stop-color="#2c3a55"/>
      </linearGradient>
    </defs>

    <!-- backdrop -->
    <rect class="backdrop" x="0" y="0" width="640" height="640" fill="var(--navy)"/>
    <rect class="floor-band" x="0" y="575" width="640" height="65" fill="var(--band)"/>

    <!-- headline -->
    <text class="headline" x="38" y="114" font-size="90" textLength="356" lengthAdjust="spacingAndGlyphs">LAUNCH</text>
    <rect class="tag-box" x="38" y="124" width="33" height="70" fill="var(--gold)"/>
    <text class="tag-your" transform="translate(62 186) rotate(-90)" textLength="56" lengthAdjust="spacingAndGlyphs">YOUR</text>
    <text class="headline" x="78" y="194" font-size="96" textLength="316" lengthAdjust="spacingAndGlyphs">BOOK</text>
    <text class="script-style" x="225" y="222" font-size="84" transform="rotate(-8 300 200)">in Style</text>

    <!-- event brand -->
    <text class="brand-name" x="519" y="96" font-size="26" text-anchor="middle" textLength="140" lengthAdjust="spacingAndGlyphs">PAGECRAFT</text>
    <text class="brand-name" x="519" y="116" font-size="11" text-anchor="middle" textLength="140" lengthAdjust="spacing">READING FAIR</text>

    <!-- author label + arrow -->
    <text class="author-name" x="518" y="194" text-anchor="middle">DR. TOBIAS</text>
    <text class="author-name" x="518" y="214" text-anchor="middle">MERRILL</text>
    <path class="pointer-arrow" d="M462 262 C455 245 456 228 466 214" fill="none" stroke="var(--pink)" stroke-width="2.5" stroke-linecap="round"/>
    <path class="pointer-head" d="M459 219 L467 212 L470 222" fill="none" stroke="var(--pink)" stroke-width="2.5" stroke-linecap="round" stroke-linejoin="round"/>

    <!-- event name -->
    <text class="event-name" x="40" y="300" textLength="216" lengthAdjust="spacingAndGlyphs">PAGECRAFT</text>
    <text class="event-name" x="40" y="338" textLength="160" lengthAdjust="spacingAndGlyphs">READING</text>
    <rect class="event-rule" x="208" y="324" width="52" height="4" fill="var(--gold)"/>
    <text class="event-name" x="40" y="376" textLength="90" lengthAdjust="spacingAndGlyphs">FAIR</text>
    <text class="event-name" x="40" y="414" textLength="118" lengthAdjust="spacingAndGlyphs">2022</text>

    <!-- date -->
    <g class="icon-calendar" fill="var(--gold)">
      <rect x="40" y="438" width="17" height="16" rx="1.5"/>
      <rect x="43" y="435" width="2.5" height="5"/>
      <rect x="51.5" y="435" width="2.5" height="5"/>
      <rect x="42" y="443" width="13" height="9" fill="var(--navy)"/>
      <rect x="43.5" y="444.5" width="3" height="2.5"/><rect x="47.5" y="444.5" width="3" height="2.5"/><rect x="51.5" y="444.5" width="3" height="2.5"/>
      <rect x="43.5" y="448.5" width="3" height="2.5"/><rect x="47.5" y="448.5" width="3" height="2.5"/>
    </g>
    <text class="detail-large" x="68" y="454">October, 7th - 8th</text>
    <rect class="detail-rule" x="40" y="461" width="232" height="1.5" fill="var(--white)"/>

    <!-- time -->
    <g class="icon-clock">
      <circle cx="49" cy="479" r="9" fill="var(--gold)"/>
      <path d="M49 473 V479 H54" fill="none" stroke="var(--navy)" stroke-width="2" stroke-linecap="round"/>
    </g>
    <text class="detail-large" x="66" y="488">8:00am - 5:00pm</text>
    <rect class="detail-rule" x="40" y="497" width="232" height="1.5" fill="var(--white)"/>

    <!-- venue -->
    <g class="icon-pin">
      <path d="M49 524 C43 516 41 513 41 509 A8 8 0 0 1 57 509 C57 513 55 516 49 524 Z" fill="var(--gold)"/>
      <circle cx="49" cy="509" r="3" fill="var(--navy)"/>
    </g>
    <text class="detail-small" x="67" y="516">Melbourne Larkfield Pavilion,</text>
    <text class="detail-small" x="67" y="533">14 Corrigan St, Southbank</text>
    <text class="detail-small" x="67" y="550">Melbourne, Australia.</text>

    <!-- ticket ribbon -->
    <g class="ticket" transform="rotate(-3 160 594)">
      <path d="M40 566 H279 V580 A7 7 0 0 0 279 594 V624 H40 V602 A7 7 0 0 0 40 588 Z" fill="var(--pink)"/>
      <text class="ticket-text" x="59" y="591">For tickets visit</text>
      <text class="ticket-text" x="59" y="609">www.quillfairhub.com.au</text>
    </g>

    <!-- book -->
    <rect class="book-shadow" x="312" y="610" width="280" height="10" rx="5" fill="#000" opacity="0.12"/>
    <rect class="book-spine-back" x="303" y="258" width="20" height="345" fill="var(--pink)"/>
    <rect class="book-spine" x="335" y="245" width="22" height="370" fill="var(--pink)"/>
    <rect class="book-cover" x="357" y="232" width="228" height="380" fill="url(#coverTone)" role="img" aria-label="Book cover of Why Comfort Costs by Tobias Merrill with author portrait"/>
  </svg>
</main>
</body>
</html>
```